Juno's Bakes Tartlets LLC website

Artisan cheesecake business looking for excellent talent to design bright, fun, engaging website for our company. We also recently acquired a food truck so we are able to cater and attend food truck events.
Our mission is to create fun, unique, delicious flavors of cheesecake and we bake them in mason jars and whole cheesecakes. We strive to exceed our customers' expectations in everything we do.
Updates
Target Market(s)
Foodies, cheesecake lovers, dessert lovers, food truck people,
Industry/Entity Type
Dessert, Catering, Pop Up events, Food truck
Coding
Coded - Design and coding required
Number of Pages Required
4 page
Requirements
Must have
- Pictures of my cheesecakes
Nice to have
- Bright, colorful, eye-catching design with a good flow

```html
<!DOCTYPE html>
<html lang="en">
<head>
<meta charset="utf-8">
<title>Juno's Bakes Tartlets LLC</title>
<link href="https://fonts.googleapis.com/css2?family=Poppins:wght@400;500;600;700;800&family=Great+Vibes&family=Allura&display=swap" rel="stylesheet">
<style>
:root{
  --pink:#f7bcc5;
  --pink-soft:#fbd7dc;
  --rose:#f2a3b0;
  --brown:#331208;
  --brown-deep:#2a0f07;
  --maroon:#6b0d18;
  --ink:#2b1a16;
  --grey:#e8e8e8;
  --white:#ffffff;
  --muted:#8a6f6a;
}
*{box-sizing:border-box;margin:0;padding:0}
html,body{width:1200px;height:4107px;overflow:hidden}
body{position:relative;font-family:'Poppins',sans-serif;color:var(--ink);background:var(--white)}
.abs{position:absolute}
.script{font-family:'Great Vibes','Allura',cursive;font-weight:400}
.btn{position:absolute;background:var(--brown);color:var(--white);border-radius:20px;font-size:14px;letter-spacing:1.5px;display:flex;align-items:center;justify-content:center;font-weight:500}
.photo{border-radius:50%;overflow:hidden}
.ring{position:absolute;border-radius:50%;border:4px solid var(--pink);padding:6px;background:var(--white)}
.ring .photo{width:100%;height:100%}
.section-title{position:absolute;left:0;width:1200px;text-align:center;font-weight:800;font-size:34px;letter-spacing:.5px}
.rule{position:absolute;left:578px;width:44px;height:3px;background:var(--rose)}
.intro{position:absolute;left:250px;width:700px;text-align:center;font-size:12.5px;line-height:16px}

/* top bar */
.topbar{left:0;top:0;width:1200px;height:60px;background:var(--pink)}
.contact-item{position:absolute;top:8px;color:var(--white);font-size:14px;line-height:15px}
.contact-item small{font-size:9px;display:block}
.contact-item svg{position:absolute;left:-40px;top:6px}
.dots{display:flex;gap:3px;margin-top:3px}
.dots i{width:14px;height:14px;border-radius:50%;background:var(--white);display:block}
.navband{left:0;top:60px;width:1200px;height:48px;background:var(--white)}
.nav{position:absolute;left:366px;top:73px;display:flex;border-bottom:1px solid var(--pink);font-size:13.5px}
.nav a{color:var(--ink);text-decoration:none;padding:2px 0;text-align:center}
.nav a.active{background:var(--pink)}
.logo{position:absolute;border-radius:50%;background:var(--pink);display:flex;flex-direction:column;align-items:center;justify-content:center;color:var(--white);font-weight:600;text-align:center;line-height:1.1}

/* hero */
.hero{left:0;top:108px;width:1200px;height:445px;background:var(--grey);overflow:hidden}
.hero h1{position:absolute;left:100px;top:88px;font-size:72px;color:var(--rose);line-height:1}
.hero .tag{position:absolute;left:100px;top:172px;font-size:37px;color:var(--rose);letter-spacing:-1px;font-weight:400}
.hero .tag b{color:var(--maroon);font-weight:800}
.hero p{position:absolute;left:103px;top:232px;width:360px;font-size:15.5px;line-height:20px}

/* about */
.about h2{position:absolute;left:625px;top:690px;font-size:35px;font-weight:800}
.about .bar{position:absolute;left:625px;top:735px;width:185px;height:2px;background:var(--maroon)}
.about p{position:absolute;left:625px;width:428px;font-size:12.5px;line-height:16.5px;text-align:justify}

/* orders */
.orders{left:0;top:1179px;width:1200px;height:711px;background:var(--pink);overflow:hidden}
.menu-head{position:absolute;font-size:54px;color:var(--ink)}
.menu-item{position:absolute;width:340px;height:60px}
.menu-item .thumb{position:absolute;left:0;top:0;width:60px;height:60px;border-radius:50%;border:3px solid var(--white)}
.menu-item h4{position:absolute;left:73px;top:4px;font-size:15px;font-weight:500}
.menu-item p{position:absolute;left:73px;top:24px;width:205px;font-size:9px;line-height:11px;color:var(--muted)}
.menu-item .price{position:absolute;left:280px;top:0;padding-left:14px;border-left:1px solid var(--ink);height:46px}
.menu-item .price b{font-size:27px;font-weight:700;display:block;line-height:34px}
.menu-item .price span{display:block;background:var(--ink);color:var(--white);font-size:6px;text-align:center;border-radius:3px;width:38px;letter-spacing:.5px}

/* events */
.event{position:absolute;width:300px;height:90px}
.cal{position:absolute;left:0;top:0;width:88px;height:84px}
.cal .day{position:absolute;left:0;top:40px;width:88px;text-align:center;font-size:22px;font-weight:800;line-height:22px;color:var(--ink)}
.cal .date{position:absolute;left:0;top:62px;width:88px;text-align:center;font-size:9px;font-weight:700}
.event h5{position:absolute;left:100px;top:0;font-size:18px;font-weight:400;color:var(--rose);line-height:18px;width:200px}
.event p{position:absolute;left:100px;top:42px;width:170px;font-size:9px;line-height:12px}

/* carousels */
.batch{left:0;top:2466px;width:1200px;height:634px;background:var(--brown-deep);overflow:hidden}
.carousel-label{position:absolute;width:240px;text-align:center;font-size:17px;font-weight:700}
.arrow{position:absolute}

/* footer */
.footer{left:0;top:3706px;width:1200px;height:355px;background:var(--brown)}
.footer .info{position:absolute;left:0;width:1200px;text-align:center;color:var(--white);font-size:13px}
.social{position:absolute;left:502px;top:3990px;display:flex;gap:8px}
.social i{width:32px;height:32px;border-radius:50%;background:var(--pink);display:block}
.copy{left:0;top:4061px;width:1200px;height:46px;background:var(--pink);text-align:center;font-size:12.5px;line-height:46px}
.blob{position:absolute;border-radius:50%}
</style>
</head>
<body>

<!-- header -->
<div class="abs topbar"></div>
<div class="contact-item" style="left:468px">
  <svg width="28" height="28" viewBox="0 0 24 24" fill="none" stroke="#fff" stroke-width="1.5"><path d="M5 3h4l2 5-2.5 1.5a11 11 0 0 0 6 6L16 13l5 2v4a2 2 0 0 1-2 2A16 16 0 0 1 3 5a2 2 0 0 1 2-2z"/></svg>
  Order Now<br>555-014-2290<small>local pick up only</small>
</div>
<div class="contact-item" style="left:667px">
  <svg width="34" height="26" viewBox="0 0 34 26" fill="none" stroke="#fff" stroke-width="1.5"><rect x="1" y="1" width="32" height="24"/><path d="M1 1l16 13L33 1"/></svg>
  Contact Email<br>hello@junosbakes.example
</div>
<div class="contact-item" style="left:837px">Follow Us<div class="dots"><i></i><i></i><i></i><i></i><i></i></div></div>

<div class="abs navband"></div>
<nav class="nav">
  <a class="active" href="#" style="width:70px">HOME</a>
  <a href="#" style="width:110px">MENU</a>
  <a href="#" style="width:90px">EVENTS</a>
  <a href="#" style="width:120px">ORDER</a>
  <a href="#" style="width:115px">ABOUT US</a>
  <a href="#" style="width:130px">CONTACT US</a>
</nav>
<div class="abs" style="left:194px;top:8px;width:160px;height:160px;border-radius:50%;background:var(--white)"></div>
<div class="logo" style="left:204px;top:18px;width:140px;height:140px;border:2px solid var(--white);box-shadow:inset 0 0 0 4px var(--pink),inset 0 0 0 6px var(--white)">
  <span style="font-size:19px">Juno's Bakes</span><span style="font-size:11px;margin-top:4px">TARTLETS</span>
</div>

<!-- hero -->
<section class="abs hero">
  <div class="blob" style="left:860px;top:-130px;width:560px;height:560px;background:var(--pink)"></div>
  <div class="blob" style="left:-110px;top:340px;width:190px;height:190px;background:var(--pink)"></div>
  <h1 class="script">Cheesecake is</h1>
  <div class="tag">A <b>LOVELIKE</b> NO OTHER.</div>
  <p>our goal is to exceed Customers'expectations and we love seeing the smiles that our cheese cakes bring to everyone!</p>
</section>
<div class="btn" style="left:100px;top:418px;width:152px;height:36px">ORDER NOW</div>
<div class="abs photo" role="img" aria-label="Whole strawberry-topped cheesecake with glaze" style="left:630px;top:118px;width:485px;height:430px;border-radius:48%;background:radial-gradient(circle at 50% 35%,#d8342d 0,#c0271f 35%,#f0e0a8 55%,#e07a3a 75%,transparent 76%)"></div>

<!-- about -->
<div class="blob" style="left:1055px;top:1005px;width:260px;height:260px;background:var(--pink-soft)"></div>
<div class="ring" style="left:109px;top:630px;width:446px;height:446px">
  <div class="photo" role="img" aria-label="The owners standing in front of the pink food truck" style="background:linear-gradient(160deg,#b7c9de 0,#e6a6c4 40%,#d88fb3 70%,#6d6a6a 100%)"></div>
</div>
<section class="about">
  <h2>ABOUT US</h2>
  <div class="bar"></div>
  <p style="top:765px">consectetur adipiscing elit. Quid autem habent admirationis, cum prope accesseris? An hoc usque quaque, aliter in vita? Non igitur de improbo, sed de callido improbo quaerimus, qualis Q. Nam quibus rebus efficiuntur voluptates, eae non sunt in potestate sapientis. Negare non possum. Huic mori optimum esse propter desperationem sapientiae, illi propter spem vivere. Quid enim me prohiberet Epicureum esse, si probarem, quae ille diceret? .</p>
  <p style="top:897px">Admirationis, cum prope accesseris? An hoc usque quaque, aliter in vita? Non igitur de improbo, sed de callido improbo quaerimus, qualis Q. Nam quibus rebus efficiuntur</p>
</section>
<div class="btn" style="left:623px;top:969px;width:153px;height:37px">READ MORE</div>

<!-- orders -->
<section class="abs orders">
  <div class="blob" style="left:-80px;top:590px;width:210px;height:210px;background:var(--pink-soft)"></div>
</section>
<div class="section-title" style="top:1248px">ORDERS</div>
<div class="rule" style="top:1303px"></div>
<p class="intro" style="top:1326px">Honestius nec turpi turpius. Tria genera bonorum Ruid iudicant sensus Suae qui&nbsp; nihil umquam magnumhonestius nec turpi turpiusbonorumiudicant&nbsp; onestius nec Verum tamen cum de rebus grandioribus dicas, ipsae res verba rapiunt; Hoc non est positum in nostra actione. Quod ea non occurrentia</p>

<div class="menu-head script" style="left:225px;top:1405px">Ordering Process</div>
<div class="menu-head script" style="left:632px;top:1405px">Payment Options</div>

<div class="menu-item" style="left:222px;top:1492px"><div class="thumb" role="img" aria-label="Strawberry cheesecake" style="background:radial-gradient(#d8342d,#f3d5a0)"></div><h4>RESPONDEAT TOTIDEM</h4><p>Ab his oratores, ab his imperatores ac rerum Omnia contraria, quos etiam insanos esse.</p><div class="price"><b>$18</b><span>STARTER</span></div></div>
<div class="menu-item" style="left:222px;top:1566px"><div class="thumb" role="img" aria-label="Chocolate cheesecake" style="background:radial-gradient(#6a3a22,#c9b8a8)"></div><h4>VERUM ETIAM PARIA</h4><p>Ab his oratores, ab his imperatores ac rerum Omnia contraria, quos etiam insanos esse.</p><div class="price"><b>$10</b><span>STARTER</span></div></div>
<div class="menu-item" style="left:222px;top:1641px"><div class="thumb" role="img" aria-label="Cheesecake slice" style="background:radial-gradient(#a7554a,#e8d3c2)"></div><h4>FUGIENDOS TRISTISSIMO</h4><p>Ab his oratores, ab his imperatores ac rerum Omnia contraria, quos etiam insanos esse.</p><div class="price"><b>$13</b><span>STARTER</span></div></div>
<div class="menu-item" style="left:222px;top:1719px"><div class="thumb" role="img" aria-label="Cookies and cream cheesecake" style="background:radial-gradient(#4a3a33,#d6cfc8)"></div><h4>VOLUPTATE SUMMUM</h4><p>Ab his oratores, ab his imperatores ac rerum Omnia contraria, quos etiam insanos esse.</p><div class="price"><b>$11</b><span>STARTER</span></div></div>

<div class="menu-item" style="left:628px;top:1492px"><div class="thumb" role="img" aria-label="Strawberry cheesecake" style="background:radial-gradient(#d8342d,#f3d5a0)"></div><h4>RESPONDEAT TOTIDEM</h4><p>Ab his oratores, ab his imperatores ac rerum Omnia contraria, quos etiam insanos esse.</p><div class="price"><b>$18</b><span>STARTER</span></div></div>
<div class="menu-item" style="left:628px;top:1566px"><div class="thumb" role="img" aria-label="Chocolate cheesecake" style="background:radial-gradient(#6a3a22,#c9b8a8)"></div><h4>VERUM ETIAM PARIA</h4><p>Ab his oratores, ab his imperatores ac rerum Omnia contraria, quos etiam insanos esse.</p><div class="price"><b>$10</b><span>STARTER</span></div></div>
<div class="menu-item" style="left:628px;top:1641px"><div class="thumb" role="img" aria-label="Cheesecake slice" style="background:radial-gradient(#a7554a,#e8d3c2)"></div><h4>FUGIENDOS TRISTISSIMO</h4><p>Ab his oratores, ab his imperatores ac rerum Omnia contraria, quos etiam insanos esse.</p><div class="price"><b>$13</b><span>STARTER</span></div></div>
<div class="menu-item" style="left:628px;top:1719px"><div class="thumb" role="img" aria-label="Cookies and cream cheesecake" style="background:radial-gradient(#4a3a33,#d6cfc8)"></div><h4>VOLUPTATE SUMMUM</h4><p>Ab his oratores, ab his imperatores ac rerum Omnia contraria, quos etiam insanos esse.</p><div class="price"><b>$11</b><span>STARTER</span></div></div>

<!-- events -->
<div class="blob" style="left:1128px;top:2280px;width:220px;height:220px;background:var(--pink-soft)"></div>
<div class="section-title" style="top:1981px">EVENTS</div>
<div class="rule" style="top:2036px"></div>

<svg width="0" height="0" style="position:absolute"><defs>
  <g id="calendar"><rect x="2" y="10" width="84" height="72" rx="6" fill="#fff" stroke="#f2a3b0" stroke-width="3"/><rect x="2" y="10" width="84" height="22" rx="6" fill="#f2a3b0"/><rect x="18" y="2" width="8" height="18" rx="4" fill="#f2a3b0" stroke="#fff" stroke-width="2"/><rect x="62" y="2" width="8" height="18" rx="4" fill="#f2a3b0" stroke="#fff" stroke-width="2"/></g>
</defs></svg>

<div class="event" style="left:99px;top:2074px"><div class="cal"><svg width="88" height="84"><use href="#calendar"/></svg><div class="day">MON</div><div class="date">10/06/2022</div></div><h5>EFFICI NTUR VOLUP DESPERATIONEM</h5><p>Verum tamen cum de rebus grandioribus dicas, ipsae res verba rapiunt; Hoc non est positum in</p></div>
<div class="event" style="left:462px;top:2074px"><div class="cal"><svg width="88" height="84"><use href="#calendar"/></svg><div class="day">TUE</div><div class="date">10/06/2022</div></div><h5>EFFICI NTUR VOLUP DESPERATIONEM</h5><p>Verum tamen cum de rebus grandioribus dicas, ipsae res verba rapiunt; Hoc non est positum in</p></div>
<div class="event" style="left:832px;top:2074px"><div class="cal"><svg width="88" height="84"><use href="#calendar"/></svg><div class="day">WED</div><div class="date">10/06/2022</div></div><h5>EFFICI NTUR VOLUP DESPERATIONEM</h5><p>Verum tamen cum de rebus grandioribus dicas, ipsae res verba rapiunt; Hoc non est positum in</p></div>
<div class="event" style="left:99px;top:2202px"><div class="cal"><svg width="88" height="84"><use href="#calendar"/></svg><div class="day">THU</div><div class="date">10/06/2022</div></div><h5>EFFICI NTUR VOLUP DESPERATIONEM</h5><p>Verum tamen cum de rebus grandioribus dicas, ipsae res verba rapiunt; Hoc non est positum in</p></div>
<div class="event" style="left:462px;top:2202px"><div class="cal"><svg width="88" height="84"><use href="#calendar"/></svg><div class="day">FRI</div><div class="date">10/06/2022</div></div><h5>EFFICI NTUR VOLUP DESPERATIONEM</h5><p>Verum tamen cum de rebus grandioribus dicas, ipsae res verba rapiunt; Hoc non est positum in</p></div>
<div class="event" style="left:832px;top:2202px"><div class="cal"><svg width="88" height="84"><use href="#calendar"/></svg><div class="day">SAT</div><div class="date">10/06/2022</div></div><h5>EFFICI NTUR VOLUP DESPERATIONEM</h5><p>Verum tamen cum de rebus grandioribus dicas, ipsae res verba rapiunt; Hoc non est positum in</p></div>
<div class="btn" style="left:524px;top:2351px;width:152px;height:35px">VIEW MORE</div>

<!-- small batch -->
<section class="abs batch">
  <div class="blob" style="left:-120px;top:470px;width:190px;height:230px;background:var(--pink)"></div>
</section>
<div class="section-title" style="top:2533px;color:var(--white)">SMALL BATCH CHEESE CAKES</div>
<div class="rule" style="top:2593px"></div>
<p class="intro" style="top:2623px;color:var(--white)">Honestius nec turpi turpius. Tria genera bonorum Ruid iudicant sensus Suae qui&nbsp; nihil umquam magnumhonestius nec turpi turpiusbonorumiudicant&nbsp; onestius nec Verum tamen cum de rebus grandioribus dicas, ipsae res verba rapiunt; Hoc non est positum in nostra actione. Quod ea non occurrentia</p>
<svg class="arrow" style="left:36px;top:2820px" width="20" height="36" viewBox="0 0 20 36" fill="none" stroke="#fff" stroke-width="2"><path d="M18 2L2 18l16 16"/></svg>
<svg class="arrow" style="left:1138px;top:2820px" width="20" height="36" viewBox="0 0 20 36" fill="none" stroke="#fff" stroke-width="2"><path d="M2 2l16 16L2 34"/></svg>
<div class="ring" style="left:98px;top:2724px;width:226px;height:226px"><div class="photo" role="img" aria-label="Strawberry cheesecakes in mason jars" style="background:radial-gradient(circle at 50% 40%,#d83a34,#e9d8c4 60%,#3a2a24)"></div></div>
<div class="ring" style="left:358px;top:2724px;width:226px;height:226px"><div class="photo" role="img" aria-label="Lemon cheesecake slice" style="background:radial-gradient(circle at 50% 45%,#f6e27a,#ecd24a 55%,#3a3430)"></div></div>
<div class="ring" style="left:618px;top:2724px;width:226px;height:226px"><div class="photo" role="img" aria-label="Chocolate ganache cheesecake with raspberries" style="background:radial-gradient(circle at 50% 45%,#6b3620,#3c1c10 60%,#2a2420)"></div></div>
<div class="ring" style="left:878px;top:2724px;width:226px;height:226px"><div class="photo" role="img" aria-label="Banana cream cheesecakes in jars" style="background:radial-gradient(circle at 50% 45%,#f3e6b8,#e7d398 55%,#bfae8a)"></div></div>
<div class="carousel-label" style="left:91px;top:2968px;color:var(--white)">DEMOCRITEUM PUTO</div>
<div class="carousel-label" style="left:351px;top:2968px;color:var(--white)">QUID TURPIUS</div>
<div class="carousel-label" style="left:611px;top:2968px;color:var(--white)">TAMEN EXPETITUR</div>
<div class="carousel-label" style="left:875px;top:2968px;color:var(--white)">QUID TURPIUS</div>

<!-- artisan -->
<div class="blob" style="left:1128px;top:3560px;width:220px;height:220px;background:var(--pink)"></div>
<div class="section-title" style="top:3166px">ARTISAN CHEESECAKES</div>
<div class="rule" style="top:3226px"></div>
<p class="intro" style="top:3255px">Honestius nec turpi turpius. Tria genera bonorum Ruid iudicant sensus Suae qui&nbsp; nihil umquam magnumhonestius nec turpi turpiusbonorumiudicant&nbsp; onestius nec Verum tamen cum de rebus grandioribus dicas, ipsae res verba rapiunt; Hoc non est positum in nostra actione. Quod ea non occurrentia</p>
<svg class="arrow" style="left:36px;top:3447px" width="20" height="36" viewBox="0 0 20 36" fill="none" stroke="#2b1a16" stroke-width="2"><path d="M18 2L2 18l16 16"/></svg>
<svg class="arrow" style="left:1138px;top:3447px" width="20" height="36" viewBox="0 0 20 36" fill="none" stroke="#2b1a16" stroke-width="2"><path d="M2 2l16 16L2 34"/></svg>
<div class="ring" style="left:98px;top:3354px;width:226px;height:226px"><div class="photo" role="img" aria-label="Whole cheesecake topped with fresh strawberries" style="background:radial-gradient(circle,#e0443a,#c22a22 60%,#f4e4d4)"></div></div>
<div class="ring" style="left:358px;top:3354px;width:226px;height:226px"><div class="photo" role="img" aria-label="Chocolate cheesecake with a cream heart" style="background:radial-gradient(circle,#f3eeee 0,#f3eeee 14%,#3a1a12 18%,#2a1008 60%,#bdbdbd)"></div></div>
<div class="ring" style="left:618px;top:3354px;width:226px;height:226px"><div class="photo" role="img" aria-label="Chocolate cheesecake decorated with pumpkins" style="background:radial-gradient(circle,#8a4a24,#4a2412 60%,#2a1a12)"></div></div>
<div class="ring" style="left:878px;top:3354px;width:226px;height:226px"><div class="photo" role="img" aria-label="Mixed berry cheesecake" style="background:radial-gradient(circle,#3a2a4a,#2a1e3a 55%,#d9a860 75%,#f1f1f1)"></div></div>
<div class="carousel-label" style="left:91px;top:3602px;color:var(--rose)">DEMOCRITEUM PUTO</div>
<div class="carousel-label" style="left:351px;top:3602px;color:var(--rose)">QUID TURPIUS</div>
<div class="carousel-label" style="left:611px;top:3602px;color:var(--rose)">TAMEN EXPETITUR</div>
<div class="carousel-label" style="left:875px;top:3602px;color:var(--rose)">QUID TURPIUS</div>

<!-- footer -->
<footer class="abs footer"></footer>
<div class="logo" style="left:512px;top:3750px;width:166px;height:166px;box-shadow:inset 0 0 0 4px var(--pink),inset 0 0 0 6px var(--white)">
  <span style="font-size:21px">Juno's Bakes</span><span style="font-size:11px;margin-top:4px">TARTLETS</span>
</div>
<div class="info" style="top:3938px">
  <svg width="10" height="12" viewBox="0 0 10 12"><path d="M5 0a4 4 0 0 1 4 4c0 3-4 8-4 8S1 7 1 4a4 4 0 0 1 4-4z" fill="#fff"/></svg>
  410 Maple Court, Juneau, Alaska 99801
</div>
<div class="info" style="top:3955px">
  <svg width="11" height="11" viewBox="0 0 24 24" fill="none" stroke="#fff" stroke-width="2"><path d="M5 3h4l2 5-2.5 1.5a11 11 0 0 0 6 6L16 13l5 2v4a2 2 0 0 1-2 2A16 16 0 0 1 3 5a2 2 0 0 1 2-2z"/></svg>555-014-2290
  <svg width="11" height="9" viewBox="0 0 11 9"><rect width="11" height="9" fill="#fff"/></svg>hello@junosbakes.example
  <svg width="10" height="10" viewBox="0 0 10 10"><circle cx="5" cy="5" r="4.5" fill="none" stroke="#fff"/></svg>junosbakes.example
</div>
<div class="social"><i></i><i></i><i></i><i></i><i></i></div>
<div class="abs copy">Copyright © 2022 Juno's Bakes Tartlets. All Right Reserved</div>

</body>
</html>
```